Psychology Practice Brochure and Letterhead
Quiet Harbor Psychological Services
I will have a submission in very shortly.
Sorry for the omission of our business contact information:
26840 W. 93rd St., Suite 410
Denbury Glen, IL 60512
Phone/Fax: 708.519.2483
info@quietharborpsych.example
#2,#7 and #8
*****Please note that we have shortened the "what to expect" section and alphabetized the items under the "what we treat" section. The new wording has been uploaded and is in the brief, along with some pictures and quotes we would like you to incorporate.
Thank you so much for your hard work on our project! We really like the green curved lines of #8 because it ties all the sections together. Could you put the "do i need therapy" section on the left outside panel? Then, you can move the "what to expect" section to the middle section with a map. Also, we really like the different shades of blue that you put behind the different text sections of #2 because it makes it easier to read.Thanks
Hello designers! We are so excited about your creative ideas for the brochure.
*****Please note that we have changed the brochure wording slightly, so please edit the text in your submissions. The changes are as follows:
1) The bullet points under "What we treat" have now been alphabetized.
2)We have shortened the "what to expect" section so that it fits better with the map on the back page of the brochure. These changes are reflected in the uploaded file called "new brochure wording."
Hello designers. Please see our design brief, as we have recently uploaded photos for you to include in the brochure. Below are some quotes that we like. Feel free to include one or two in the brochure.
"A journey of a thousand miles begins with a single step." Wen Shaoli
"I am not what happens to me, I am what I choose to become." Emil Dorst
"Life is not about who you once were, it is about who you are right now, and the person you have the potential to become." Unknown
We have identified a number of photos and quotes from various sites that we might want to use, but don't want to buy them all in case they don't ultimately work in the design. Is it ok to upload them, but then buy them if they are used?
Drafts #2 and #5: Could you incorporate both blue and green?
draft #5: thank you for your submission. Could we see the design without the pictures of physicians in lab coats? Instead, we would like to see pictures of adults, children or families. Having some pictures of people looking unhappy, angry or stressed is fine along with happier pictures, as well. Any quotes about happiness or hopefulness would also be welcome.
draft #2: Thank you for your submission. Could you replace the picture of the older couple and replace it with children or teens? Also, could you show us another option for the layout on the interior? Or, another way of separating the sections that doesn't use the solid lines?
draft #1: Thank you for your submission. We like the way you've used blue and green throughout the brochure, and the addition of the tree was nice. Is there a way to reduce the quantity of brown used? Also, could you give us some additional variety in the pictures used, such as some in which the people are not jumping?
Do you have any website?
we need vector logo! please upload it!

```html
<!DOCTYPE html>
<html lang="en">
<head>
<meta charset="utf-8">
<title>Quiet Harbor Psychological Services – Brochure and Letterhead</title>
<link href="https://fonts.googleapis.com/css2?family=Crimson+Text:ital,wght@0,400;0,700;1,400&family=Open+Sans:wght@400;600;700&display=swap" rel="stylesheet">
<style>
:root{
  --stage:#5a3a22;
  --navy:#1c4b86;
  --blue:#2d7cc0;
  --sky:#7bb8e2;
  --pale:#dcecf8;
  --green:#4f9d2e;
  --lime:#a9d36b;
  --ink:#33414f;
  --white:#ffffff;
  --label:#f1e6d6;
}
*{box-sizing:border-box;margin:0;padding:0}
html,body{width:1200px;height:835px;overflow:hidden;background:var(--stage)}
body{position:relative;font-family:"Open Sans",Arial,sans-serif;color:var(--ink)}
.piece{position:absolute;overflow:hidden;background:var(--white);box-shadow:0 3px 10px rgba(0,0,0,.45)}
.label{position:absolute;font-size:9px;color:var(--label);text-align:center}
.panel{position:absolute;top:0;height:100%;overflow:hidden}
.photo{position:absolute}
.serif{font-family:"Crimson Text",Georgia,serif}
.small{font-size:5px;line-height:1.45}
.small p{margin-bottom:4px}
.head-navy{font-family:"Crimson Text",Georgia,serif;font-weight:700;color:var(--navy)}
.brand{font-family:"Crimson Text",Georgia,serif;font-weight:700;display:flex;align-items:center;gap:5px}
.brand .dot{width:9px;height:9px;border-radius:50%;flex:none}
/* expect panel */
.expect{background:linear-gradient(180deg,var(--blue),var(--navy));color:var(--white);padding:34px 12px 0}
.expect h3{font-family:"Crimson Text",Georgia,serif;font-size:10px;margin-bottom:4px}
.expect .cta{font-family:"Crimson Text",Georgia,serif;font-size:10px;line-height:1.2;margin:8px 0 6px;text-align:center}
.expect .phone{font-size:13px;font-weight:700;text-align:center}
.expect .contact{font-size:5.5px;text-align:center;line-height:1.5;margin-top:3px}
.expect .map{position:absolute;left:10px;right:10px;bottom:14px;height:70px;background:linear-gradient(135deg,#e4e8dc,#c9d6c4);border:2px solid var(--white)}
/* cover panel */
.cover{background:var(--white)}
.cover .band{position:absolute;left:0;right:0;top:0;height:72px;background:linear-gradient(180deg,var(--navy),var(--blue));color:var(--white);padding:12px 14px;text-align:right}
.cover .band q{font-family:"Crimson Text",Georgia,serif;font-style:italic;font-size:11px;line-height:1.15;quotes:none;display:block}
.cover .band cite{font-size:5px;font-style:normal}
.cover .photo{left:0;right:0;top:72px;height:180px;background:linear-gradient(160deg,#8ec3e8,#e3b98c 60%,#6aa0c8)}
.cover .brandbox{position:absolute;left:0;right:0;bottom:18px;text-align:center}
.cover .brand{justify-content:center;color:var(--navy);font-size:12px;line-height:1.05;text-align:left}
.curve{position:absolute;left:0;width:100%}
ul.list{list-style:none;font-size:5.5px;line-height:1.55}
ul.list li::before{content:"• ";color:var(--green)}
/* letterhead */
.lh-contact{position:absolute;right:20px;top:14px;text-align:right;font-size:6px;line-height:1.45}
.lh-contact .lh-phone{font-size:9px;font-weight:700;color:var(--navy)}
</style>
</head>
<body>

<!-- Outside spread -->
<section class="piece outside" style="left:41px;top:12px;width:504px;height:384px">
  <div class="panel need" style="left:0;width:168px">
    <div class="photo" role="img" aria-label="Photo of a stressed woman holding her head" style="left:0;top:0;width:168px;height:108px;background:linear-gradient(135deg,#b8c9d6,#6f8aa3)"></div>
    <svg class="curve" style="top:94px" width="168" height="20" viewBox="0 0 168 20"><path d="M0 20 Q70 -4 168 8 L168 20Z" fill="var(--white)"/><path d="M0 16 Q70 -4 168 6" fill="none" stroke="var(--green)" stroke-width="2"/></svg>
    <h2 class="head-navy" style="position:absolute;left:12px;top:116px;font-size:16px;line-height:1">Do I Need<br>Therapy?</h2>
    <div class="small" style="position:absolute;left:12px;right:12px;top:156px">
      <p>Most people experience emotional strain, conflict or hard times. It can help to talk with a trained professional when these feel heavy.</p>
      <p>You may benefit if you feel stuck, anxious or overwhelmed for weeks at a time.</p>
      <p>If sleep, appetite or mood have changed, or daily tasks feel harder than before, it may be time to reach out.</p>
      <p>Family conflict, loss, school trouble or big life changes are all good reasons to begin.</p>
      <p>Therapy is not only for crisis. Many people come to grow, learn new skills and feel more settled.</p>
      <p>Whether you are struggling with a short-term issue or a long-standing one, we are here to help.</p>
    </div>
  </div>
  <div class="panel expect" style="left:168px;width:168px">
    <svg class="curve" style="top:0" width="168" height="30" viewBox="0 0 168 30"><path d="M0 0 H168 V14 Q90 34 0 12Z" fill="var(--white)"/><path d="M0 14 Q90 36 168 16" fill="none" stroke="var(--lime)" stroke-width="2"/></svg>
    <h3>What To Expect:</h3>
    <p class="small">During the first session, you and a therapist will talk about what brings you in and set goals together. We will plan care that fits your needs, your pace and your family.</p>
    <p class="cta">Take the first step toward a better tomorrow and give us a call today.</p>
    <p class="phone">708.519.2483</p>
    <p class="contact">Email<br>info@quietharborpsych.example</p>
    <p class="contact" style="margin-top:6px">Quiet Harbor Psychological Services<br>26840 W. 93rd St., Suite 410<br>Denbury Glen, IL 60512</p>
    <div class="map" role="img" aria-label="Street map showing the office location"></div>
  </div>
  <div class="panel cover" style="left:336px;width:168px">
    <div class="band"><q>A journey of a thousand miles begins with a single step.</q><cite>— Wen Shaoli</cite></div>
    <div class="photo" role="img" aria-label="Photo of a smiling family playing outdoors"></div>
    <svg class="curve" style="top:228px" width="168" height="40" viewBox="0 0 168 40"><path d="M0 40 V22 Q84 -4 168 18 V40Z" fill="var(--white)"/><path d="M0 20 Q84 -6 168 16" fill="none" stroke="var(--green)" stroke-width="3"/><path d="M0 27 Q84 2 168 24" fill="none" stroke="var(--lime)" stroke-width="2"/></svg>
    <div class="brandbox"><div class="brand"><span class="dot" style="background:var(--green)"></span><span>Quiet Harbor<br><span style="font-size:8px">Psychological Services</span></span></div></div>
  </div>
</section>
<div class="label" style="left:41px;top:402px;width:504px">Outside</div>

<!-- Front fold -->
<section class="piece" style="left:576px;top:12px;width:187px;height:384px">
  <div class="panel cover" style="left:0;width:187px">
    <div class="band"><q>A journey of a thousand miles begins with a single step.</q><cite>— Wen Shaoli</cite></div>
    <div class="photo" role="img" aria-label="Photo of a smiling family playing outdoors"></div>
    <svg class="curve" style="top:228px" width="187" height="40" viewBox="0 0 187 40"><path d="M0 40 V22 Q94 -4 187 18 V40Z" fill="var(--white)"/><path d="M0 20 Q94 -6 187 16" fill="none" stroke="var(--green)" stroke-width="3"/><path d="M0 27 Q94 2 187 24" fill="none" stroke="var(--lime)" stroke-width="2"/></svg>
    <div class="brandbox"><div class="brand"><span class="dot" style="background:var(--green)"></span><span>Quiet Harbor<br><span style="font-size:8px">Psychological Services</span></span></div></div>
  </div>
</section>
<div class="label" style="left:576px;top:402px;width:187px">Front Fold</div>

<!-- Inside spread -->
<section class="piece inside" style="left:41px;top:432px;width:504px;height:384px">
  <div class="photo" role="img" aria-label="Photo of a young person looking thoughtful" style="left:0;top:0;width:168px;height:150px;background:linear-gradient(160deg,#cfe3f2,#8fb6d6)"></div>
  <div style="position:absolute;left:168px;top:0;width:336px;height:150px;background:linear-gradient(180deg,var(--sky),var(--blue));color:var(--white);padding:16px 16px">
    <h2 class="serif" style="font-size:13px;font-weight:700;margin-bottom:4px">Philosophy</h2>
    <p class="small" style="width:200px">We believe every person has the strength to grow. Our team offers warm, practical care for children, teens, adults and families, and we work with you to build skills, ease distress and find a path forward.</p>
  </div>
  <svg class="curve" style="top:120px" width="504" height="40" viewBox="0 0 504 40"><path d="M0 40 V24 Q250 -6 504 22 V40Z" fill="var(--white)"/><path d="M0 22 Q250 -8 504 20" fill="none" stroke="var(--green)" stroke-width="3"/></svg>
  <div style="position:absolute;left:12px;top:160px;width:150px">
    <h3 class="head-navy" style="font-size:13px;margin-bottom:3px">How We Help</h3>
    <p class="small" style="margin-bottom:4px">Quiet Harbor offers a range of services to meet your needs:</p>
    <ul class="list">
      <li>Individual Therapy</li><li>Child and Adolescent Therapy</li><li>Couples/Family Therapy</li><li>Parent Coaching</li><li>Psychological and Neuropsychological Testing</li>
    </ul>
  </div>
  <div class="photo" role="img" aria-label="Photo of a person resting on a park bench under open sky" style="left:176px;top:150px;width:160px;height:100px;background:linear-gradient(180deg,#bcdcf2,#e8eef0 70%,#a7c98a)"></div>
  <p class="serif" style="position:absolute;left:186px;top:160px;width:110px;font-style:italic;font-size:8px;line-height:1.2;color:var(--white)">“Life is not about who you once were, it is about who you are right now, and the person you have the potential to become.”</p>
  <div class="photo" role="img" aria-label="Photo of a smiling child" style="left:344px;top:160px;width:150px;height:90px;background:linear-gradient(135deg,#f0d2b4,#c99a77)"></div>
  <div style="position:absolute;left:0;top:258px;width:380px;height:126px;background:linear-gradient(180deg,var(--pale),var(--white));padding:8px 12px">
    <h3 class="head-navy" style="font-size:12px">What We Treat</h3>
    <p class="small">Some specific problems that we can help with are:</p>
    <div style="display:flex;gap:20px;margin-top:3px">
      <ul class="list"><li>Anxiety, Panic, Phobias</li><li>Attention Deficit Disorder</li><li>Behavior Problems</li><li>Communication and Emotional Development</li><li>Depression, Mood Disorders</li><li>Grief or Relationship Loss</li></ul>
      <ul class="list"><li>Learning Disabilities</li><li>Parenting Concerns</li><li>School Problems</li><li>Self-Esteem Issues</li><li>Social Skills Development</li><li>Stress Management</li></ul>
    </div>
  </div>
  <div class="photo" role="img" aria-label="Photo of white daisies in a green field" style="left:380px;top:258px;width:124px;height:126px;background:linear-gradient(180deg,#9fcfe8,#8fc265 60%,#5e9a3d)"></div>
</section>
<div class="label" style="left:41px;top:820px;width:504px">Inside</div>

<!-- Back fold -->
<section class="piece" style="left:576px;top:432px;width:187px;height:372px">
  <div class="panel expect" style="left:0;width:187px">
    <svg class="curve" style="top:0" width="187" height="30" viewBox="0 0 187 30"><path d="M0 0 H187 V14 Q100 34 0 12Z" fill="var(--white)"/><path d="M0 14 Q100 36 187 16" fill="none" stroke="var(--lime)" stroke-width="2"/></svg>
    <h3>What To Expect:</h3>
    <p class="small">During the first session, you and a therapist will talk about what brings you in and set goals together. We will plan care that fits your needs, your pace and your family.</p>
    <p class="cta">Take the first step toward a better tomorrow and give us a call today.</p>
    <p class="phone">708.519.2483</p>
    <p class="contact">Email<br>info@quietharborpsych.example</p>
    <p class="contact" style="margin-top:6px">Quiet Harbor Psychological Services<br>26840 W. 93rd St., Suite 410<br>Denbury Glen, IL 60512</p>
    <div class="map" role="img" aria-label="Street map showing the office location"></div>
  </div>
</section>
<div class="label" style="left:576px;top:808px;width:187px">Back Fold</div>

<!-- Letterhead -->
<section class="piece letterhead" style="left:804px;top:156px;width:372px;height:504px">
  <div class="brand" style="position:absolute;left:20px;top:18px;color:var(--navy);font-size:14px;line-height:1.05"><span class="dot" style="background:var(--green)"></span><span>Quiet Harbor<br><span style="font-size:8px">Psychological Services</span></span></div>
  <div class="lh-contact">
    <div class="lh-phone">Phone/Fax: 708.519.2483</div>
    <div>Email: info@quietharborpsych.example</div>
    <div style="margin-top:3px">Quiet Harbor Psychological Services</div>
    <div>26840 W. 93rd St., Suite 410, Denbury Glen, IL 60512</div>
  </div>
  <svg class="curve" style="top:66px" width="372" height="24" viewBox="0 0 372 24"><path d="M0 18 Q180 -6 372 10" fill="none" stroke="var(--green)" stroke-width="3"/><path d="M0 22 Q180 2 372 16" fill="none" stroke="var(--sky)" stroke-width="2"/></svg>
  <div style="position:absolute;left:20px;right:20px;top:418px;display:flex;gap:20px;font-size:5px;line-height:1.5;color:var(--navy)">
    <div>Anxiety, Panic, Phobias and Obsessive Compulsive<br>Attention Deficit Disorder<br>Behavior Problems<br>Communication and Emotional Development<br>Depression, Mood Disorders</div>
    <div>Learning Disabilities<br>Parenting Concerns<br>School Problems<br>Self-Esteem Issues<br>Social Skills and Stress Management</div>
  </div>
  <svg class="curve" style="bottom:0" width="372" height="34" viewBox="0 0 372 34"><path d="M0 34 V16 Q190 -6 372 14 V34Z" fill="var(--blue)"/><path d="M0 12 Q190 -8 372 10" fill="none" stroke="var(--green)" stroke-width="2"/></svg>
</section>
<div class="label" style="left:804px;top:668px;width:372px">Letterhead</div>

</body>
</html>
```